Business Card design for new private practice opening

I need a business card design for my new private practice with my new logo uploaded as a file
On the front the logo
On the back: maybe a small logo somewhere?
Priv. Doz. DDr. Petra Sommerfeld
Fachärztin für Allgemein- & Viszeralchirurgie
Address: xxx
Tel: xxx
Mobil:xxx
Webseite:xxx
Email:xxx

Contact Information for Business Card

See project description above for details

Requirements
Nice to have
• I would like the colors of the logo incorporated into the business card

```html
<!DOCTYPE html>
<html lang="de">
<head>
<meta charset="utf-8">
<title>Sommerfeld Chirurgie – Visitenkarte</title>
<link href="https://fonts.googleapis.com/css2?family=Montserrat:wght@600&family=Nunito:wght@400;700&display=swap" rel="stylesheet">
<style>
  :root {
    --backdrop: #efebe8;
    --card: #ffffff;
    --teal: #5fb2b2;
    --grey: #7b7b7b;
    --grey-dark: #6a6a6a;
    --shadow: rgba(0,0,0,0.10);
  }
  * { box-sizing: border-box; margin: 0; padding: 0; }
  html, body { width: 1200px; height: 800px; overflow: hidden; }
  body { background: var(--backdrop); position: relative; font-family: "Nunito", sans-serif; }

  .card {
    position: absolute;
    width: 520px; height: 320px;
    background: var(--card);
    box-shadow: 0 6px 18px var(--shadow);
  }

  /* Front */
  .card--front { left: 70px; top: 80px; }
  .front-mark {
    position: absolute; left: 50%; top: 52px; transform: translateX(-50%);
    width: 150px; height: 126px; border-radius: 50%;
    border: 6px solid var(--grey);
    background: var(--teal);
  }
  .front-name {
    position: absolute; left: 0; right: 0; top: 206px; text-align: center;
    font-family: "Montserrat", sans-serif; font-weight: 600;
    font-size: 30px; letter-spacing: 0.5px; color: var(--grey);
  }
  .front-rule {
    position: absolute; left: 70px; right: 70px; top: 272px;
    height: 2px; background: var(--teal);
  }

  /* Back */
  .card--back { left: 610px; top: 400px; }
  .back-mark {
    position: absolute; left: 36px; top: 36px;
    width: 96px; height: 86px; border-radius: 50%;
    border: 4px solid var(--grey);
    background: var(--teal);
  }
  .back-name {
    position: absolute; left: 150px; top: 46px;
    font-family: "Nunito", sans-serif; font-weight: 700;
    font-size: 20px; color: var(--grey-dark);
  }
  .back-title {
    position: absolute; left: 150px; top: 80px;
    font-size: 15px; color: var(--grey);
  }
  .back-rule {
    position: absolute; left: 30px; right: 30px; height: 1.5px; background: var(--teal);
  }
  .back-rule--top { top: 140px; }
  .back-rule--bottom { top: 290px; }

  .contacts {
    position: absolute; top: 160px; list-style: none;
    display: flex; flex-direction: column; gap: 9px;
  }
  .contacts--left { left: 36px; }
  .contacts--right { left: 290px; }
  .contact {
    display: flex; align-items: center; gap: 10px;
    font-size: 16px; color: var(--grey-dark); height: 22px;
  }
  .contact svg { width: 20px; height: 20px; flex: none; }
  .icon { fill: none; stroke: var(--teal); stroke-width: 1.8; stroke-linecap: round; stroke-linejoin: round; }
  .icon-fill { fill: var(--teal); }
</style>
</head>
<body>

<section class="card card--front" aria-label="Vorderseite">
  <div class="front-mark"></div>
  <h1 class="front-name">SOMMERFELD CHIRURGIE</h1>
  <div class="front-rule"></div>
</section>

<section class="card card--back" aria-label="Rückseite">
  <div class="back-mark"></div>
  <h2 class="back-name">Priv. Doz. DDr. Petra Sommerfeld</h2>
  <p class="back-title">Fachärztin für Allgemein- &amp; Viszeralchirurgie</p>
  <div class="back-rule back-rule--top"></div>

  <ul class="contacts contacts--left">
    <li class="contact">
      <svg viewBox="0 0 20 20"><path class="icon-fill" d="M10 1.5a6 6 0 0 0-6 6c0 4.5 6 11 6 11s6-6.5 6-11a6 6 0 0 0-6-6zm0 8.5a2.5 2.5 0 1 1 0-5 2.5 2.5 0 0 1 0 5z"/></svg>
      <span>xxx</span>
    </li>
    <li class="contact">
      <svg viewBox="0 0 20 20"><path class="icon-fill" d="M5 2l3 3.5-1.6 2.2a11 11 0 0 0 5.9 5.9l2.2-1.6L18 15l-2 3C9 18 2 11 2 4z"/></svg>
      <span>Tel: xxx</span>
    </li>
    <li class="contact">
      <svg viewBox="0 0 20 20"><g class="icon"><circle cx="10" cy="10" r="8"/><path d="M2 10h16M10 2c3 3 3 13 0 16M10 2c-3 3-3 13 0 16"/></g></svg>
      <span>Mobil: xxx</span>
    </li>
    <li class="contact">
      <svg viewBox="0 0 20 20"><g class="icon"><rect x="2" y="4" width="16" height="12" rx="1"/><path d="M2.5 4.5L10 11l7.5-6.5"/></g></svg>
      <span>Email: xxx</span>
    </li>
  </ul>

  <ul class="contacts contacts--right">
    <li class="contact">
      <svg viewBox="0 0 20 20"><g class="icon"><rect x="5" y="1.5" width="10" height="17" rx="2"/><path d="M8.5 15.5h3"/></g></svg>
      <span>Mobil: xxx</span>
    </li>
    <li class="contact">
      <svg viewBox="0 0 20 20"><g class="icon"><circle cx="10" cy="10" r="8"/><path d="M2 10h16M10 2c3 3 3 13 0 16M10 2c-3 3-3 13 0 16"/></g></svg>
      <span>Webseite: xxx</span>
    </li>
    <li class="contact">
      <svg viewBox="0 0 20 20"><g class="icon"><rect x="2" y="4" width="16" height="12" rx="1"/><path d="M2.5 4.5L10 11l7.5-6.5"/></g></svg>
      <span>Email: xxx</span>
    </li>
  </ul>

  <div class="back-rule back-rule--bottom"></div>
</section>

</body>
</html>
```